The Polish & Sugar Loft Website Update

Hello. I am seeking to freshen up my website with a clean and easy feel that incorporates our modern chic style. Our services cater to mostly young professionals and modern moms.

We focus on natural nail care and gentle professional waxing. We are known for our cleanliness. Our clients like our current website, however I'm hoping to make it look even more professional and user friendly. Some clients have even said our current website feels welcoming, unlike other websites that in they feel give a snobbish vibe. I like clean lines, simple, fresh, and sometimes bold. Totally NOT a fan of whimsical.

I threw added an accent color to the color pallet...however it should be used in moderation. I am also open to other accent colors. I'd like the site to emphasize the Brazilian wax as much as nails, if not more than nail. The photos downloaded are just to give you a few images of who we are, however are not necessary. Current website www.polishsugarloft-demo.com

Target Market(s)

Females 30-55

Industry/Entity Type

Beauty Salon

Coding

Coded - Design and coding required

Number of Pages Required

5+ page

Font styles to use
Sans Serif

Colors
ffffff
1b1b1b
acd136
eeeeee
878787
c4c4c4
efefef
7f7f7f

Requirements
Must have
• Clean look
Nice to have
• Our logo
Should not have
• Whimsical

```html
<!DOCTYPE html>
<html lang="en">
<head>
<meta charset="utf-8">
<title>The Polish &amp; Sugar Loft</title>
<link href="https://fonts.googleapis.com/css2?family=Roboto:ital,wght@0,300;0,400;0,500;1,400&display=swap" rel="stylesheet">
<style>
:root{
  --white:#ffffff;
  --ink:#1b1b1b;
  --green:#acd136;
  --grey-light:#eeeeee;
  --grey-band:#ebebeb;
  --grey-text:#555555;
  --grey-mid:#878787;
  --grey-line:#c4c4c4;
  --nav:#4a4a4a;
  --accent:#e5401f;
}
*{margin:0;padding:0;box-sizing:border-box}
html,body{width:1200px;height:2329px;overflow:hidden}
body{position:relative;background:var(--white);font-family:'Roboto',sans-serif;color:var(--ink)}
.abs{position:absolute}
.site-header{left:0;top:0;width:1200px;height:118px;background:var(--white)}
.brand{left:75px;top:38px;font-size:30px;font-weight:400;color:#3a3a3a;letter-spacing:.5px;display:flex;align-items:center;gap:12px}
.brand-mark{width:18px;height:18px;border-radius:50%;background:var(--green)}
.gift-text{left:900px;top:36px;width:131px;text-align:right;font-size:14px;line-height:19px;color:var(--ink)}
.gift-card{left:1049px;top:28px;width:75px;height:56px;background:linear-gradient(135deg,#c8161c,#e8e2dc 60%)}
.main-nav{left:0;top:118px;width:1200px;height:61px;background:var(--nav)}
.nav-item{top:0;height:61px;line-height:61px;font-size:13px;color:var(--white);text-transform:uppercase;white-space:nowrap}
.nav-item.active{background:var(--green);text-align:center}
.hero{left:0;top:179px;width:1200px;height:546px;background:linear-gradient(180deg,#5d5a57 0%,#3c3936 55%,#2a2826 100%)}
.hero-title{left:0;top:380px;width:1200px;text-align:center;font-size:44px;font-weight:500;color:var(--white);letter-spacing:1px}
.hero-title span{color:var(--green)}
.hero-sub{left:230px;top:449px;width:740px;text-align:center;font-size:15px;line-height:20px;color:var(--white)}
.hero-arrow{left:45px;top:426px}
.hero-arrow-right{left:1107px;top:426px;opacity:.25}
.section-title{left:0;width:1200px;text-align:center;font-size:29px;font-weight:400;color:var(--ink)}
.section-sub{left:230px;width:740px;text-align:center;font-size:14px;line-height:20px;color:#444}
.photo{background:#ddd}
.nail-photo{left:85px;top:944px;width:356px;height:352px;background:linear-gradient(160deg,#f1ece8,#d9c7c0 55%,#eae6e3)}
.wax-photo{left:711px;top:944px;width:342px;height:341px;border:1px solid #e2e2e2;background:linear-gradient(180deg,#fff 0%,#f3ebe6 40%,#f7f3f0)}
.price-box{background:rgba(238,238,238,.92)}
.nail-box{left:382px;top:1020px;width:293px;height:194px}
.wax-box{left:832px;top:1226px;width:280px;height:194px;background:#e6e6e6}
.service-name{font-size:22px;color:var(--accent);text-align:center}
.service-rule{height:2px;width:32px;background:var(--accent)}
.price-list{list-style:none;text-align:center;font-size:15px;line-height:28px;color:#222}
.know-more{font-size:12px;color:var(--accent);text-transform:uppercase;text-align:center;letter-spacing:.4px}
.mission{left:0;top:1481px;width:1200px;height:320px;background:var(--grey-band)}
.mission-text{left:106px;width:988px;text-align:center;font-size:13px;line-height:19px;color:var(--grey-text)}
.btn{left:511px;top:1714px;width:180px;height:45px;background:var(--accent);color:var(--white);font-size:16px;line-height:45px;text-align:center}
.title-rule{left:584px;width:32px;height:2px;background:var(--accent)}
.review-card{top:1926px;width:324px;height:100px;border:1px solid #d8d8d8;padding:17px 22px;font-size:13px;line-height:20px;font-style:italic;color:#444;text-align:justify}
.avatar{width:66px;height:66px;border-radius:50%;background:linear-gradient(180deg,#b9b4ad,#6f6a66)}
.author{font-size:15px;color:var(--accent)}
.author-loc{font-size:12px;font-style:italic;color:var(--grey-mid)}
.site-footer{left:0;top:2162px;width:1200px;height:167px;background:var(--green)}
.social{top:2202px;width:30px;height:30px;border-radius:50%;background:var(--white)}
.footer-links{left:0;top:2250px;width:1200px;text-align:center;font-size:14px;color:var(--white)}
.footer-links span{margin:0 9px}
.copyright{left:0;top:2276px;width:1200px;text-align:center;font-size:12px;color:var(--white)}
</style>
</head>
<body>
<header class="abs site-header">
  <div class="abs brand"><span class="brand-mark"></span>The Polish &amp; Sugar Loft</div>
  <div class="abs gift-text">Purchase Gift Cards Online</div>
  <div class="abs gift-card" role="img" aria-label="Gift card with red ribbon bow"></div>
</header>
<nav class="abs main-nav">
  <div class="abs nav-item active" style="left:75px;width:97px">Home</div>
  <div class="abs nav-item" style="left:203px">Schedule an Appointment</div>
  <div class="abs nav-item" style="left:427px">Products &amp; Services</div>
  <div class="abs nav-item" style="left:612px">Careers</div>
  <div class="abs nav-item" style="left:711px">Specials</div>
  <div class="abs nav-item" style="left:812px">About Us</div>
  <div class="abs nav-item" style="left:917px">FAQ</div>
  <div class="abs nav-item" style="left:978px">Contact Us</div>
</nav>
<section class="abs hero" role="img" aria-label="Salon interior with polish shelves, manicure stations and pedicure chairs"></section>
<h1 class="abs hero-title">WE <span>ENHANCE</span> YOUR <span>BEAUTY</span></h1>
<p class="abs hero-sub">Sed ut perspiciatis unde omnis iste natus error sit voluptatem accusantium doloremque laudantium, totam rem aperiam eaque ipsa quae ab illo inventore veritatis.</p>
<svg class="abs hero-arrow" width="46" height="46" viewBox="0 0 46 46"><circle cx="23" cy="23" r="23" fill="#fff"/><path d="M26 15 L18 23 L26 31" fill="none" stroke="#333" stroke-width="4"/></svg>
<svg class="abs hero-arrow-right" width="46" height="46" viewBox="0 0 46 46"><circle cx="23" cy="23" r="23" fill="#fff"/><path d="M20 15 L28 23 L20 31" fill="none" stroke="#333" stroke-width="4"/></svg>

<h2 class="abs section-title" style="top:800px">OUR SERVICES</h2>
<p class="abs section-sub" style="top:850px">Sed ut perspiciatis unde omnis iste natus error sit voluptatem accusantium doloremque laudantium, totam rem aperiam eaque ipsa quae ab illo inventore veritatis.</p>

<div class="abs nail-photo" role="img" aria-label="Hands with a fresh French manicure on a white towel"></div>
<div class="abs price-box nail-box"></div>
<div class="abs service-name" style="left:454px;top:962px;width:200px">Nail Care</div>
<div class="abs service-rule" style="left:538px;top:997px"></div>
<ul class="abs price-list" style="left:382px;top:1043px;width:293px">
  <li>Signature Manicure - $24</li>
  <li>Lumiere Gel Manicure - $34</li>
  <li>Signature Pedicure - $40</li>
</ul>
<div class="abs know-more" style="left:382px;top:1144px;width:293px">Know More</div>

<div class="abs wax-photo" role="img" aria-label="Woman in white sports top and briefs, smooth skin after waxing"></div>
<div class="abs price-box wax-box"></div>
<div class="abs service-name" style="left:672px;top:1314px;width:200px">Wax</div>
<div class="abs service-rule" style="left:756px;top:1350px"></div>
<ul class="abs price-list" style="left:832px;top:1255px;width:280px">
  <li>Brow Design - $13</li>
  <li>Chin - $10</li>
  <li>Lip - $10</li>
  <li>Brazilian $55</li>
</ul>
<div class="abs know-more" style="left:832px;top:1374px;width:280px">Know More</div>

<section class="abs mission"></section>
<h2 class="abs section-title" style="top:1530px">OUR MISSION</h2>
<p class="abs mission-text" style="top:1580px">To be the #1 nail and wax salon in the Brookhaven Falls area, offering the most meticulous manicures, pedicures, and waxing service. We use superior products, advanced techniques, and exceptional sanitation procedures to provide our clients with safe, quality services. Our knowledgeable and friendly staff is always happy to assist with any of your Polish &amp; Sugar concerns.</p>
<p class="abs mission-text" style="top:1654px">We are excited to welcome another Licensed Nail Technician to our team, Dana Whitfield. Dana has over 25 years experience and is also a certified Medical Nail Technician. You will love her spunk and genuine friendliness. If you're seeking a perfect mani, Dana is your girl.</p>
<div class="abs btn">Make Appointment</div>

<h2 class="abs section-title" style="top:1856px">CUSTOMER REVIEWS</h2>
<div class="abs title-rule" style="top:1895px"></div>

<blockquote class="abs review-card" style="left:73px">"Sed ut perspiciatis unde omnis iste natus error sit volup tatem accusa ntium dolore mque laudantium totam rem aperiam"</blockquote>
<div class="abs avatar" style="left:71px;top:2042px" role="img" aria-label="Reviewer portrait"></div>
<div class="abs author" style="left:151px;top:2054px">By Author Name</div>
<div class="abs author-loc" style="left:151px;top:2074px">city, location</div>

<blockquote class="abs review-card" style="left:436px">"Sed ut perspiciatis unde omnis iste natus error sit volup tatem accusa ntium dolore mque laudantium totam rem aperiam"</blockquote>
<div class="abs avatar" style="left:434px;top:2042px" role="img" aria-label="Reviewer portrait"></div>
<div class="abs author" style="left:514px;top:2054px">By Author Name</div>
<div class="abs author-loc" style="left:514px;top:2074px">city, location</div>

<blockquote class="abs review-card" style="left:798px">"Sed ut perspiciatis unde omnis iste natus error sit volup tatem accusa ntium dolore mque laudantium totam rem aperiam"</blockquote>
<div class="abs avatar" style="left:796px;top:2042px" role="img" aria-label="Reviewer portrait"></div>
<div class="abs author" style="left:876px;top:2054px">By Author Name</div>
<div class="abs author-loc" style="left:876px;top:2074px">city, location</div>

<footer class="abs site-footer"></footer>
<div class="abs social" style="left:508px"></div>
<div class="abs social" style="left:547px"></div>
<div class="abs social" style="left:586px"></div>
<div class="abs social" style="left:624px"></div>
<div class="abs social" style="left:663px"></div>
<div class="abs footer-links">Home<span>|</span>Schedule An Appointment<span>|</span>Products &amp; Services<span>|</span>Careers<span>|</span>Specials<span>|</span>About Us<span>|</span>FAQ<span>|</span>Contact Us</div>
<div class="abs copyright">Copyright 2016 The Polish &amp; Sugar Loft. All rights reserved.</div>
</body>
</html>
```